High Profile Wordpress Design for Marketing Agency

http://www.LanternCo.example.nz is moving from GridPortal to wordpress

Lantern Co is a leading New Zealand consumer brands public relations and advertising agency.
Our marketing agency represents some of the worlds most recognisable brands as well as some small independent businesses and everything in between.
Our GPL current site has served us well for 6+ years but we are now wanting to move to wordpress.

We are looking for a new look for our website which will be either a 2013 facelift keeping existing colour scheme rather than a radical new design
Our target market is marketing managers and brand owners familiar with design and marketing elements.
First and foremost the site must be functional from an SEO and loading speed point of view. To assist this we want to retain the text content.
Secondly we have historically had only pointers to other pages on our site but we want to incorporate more of the highlights of our services and our portfolio with the addition of some 'sample boxes' such as in this template: http://vendorplace.example/item/sample-business-theme/full_screen_preview/5821307

Wordpress offers an easier interface for uploading news items which we do daily and also take advantage of the plugins for seo. We are looking to redesign the look of the site while keeping all the existing text content.

Logo – also needs refreshing. Something corporate but not staid. Modern and clean.

Existing pages
- We want a fresh new clean look while retaining the orange and gray colours. white space is good. modern fonts are good.
- Social media : we want to focus on Google Plus primarily but also facebook and twitter. We suggest a funky design with the social media logos. Social media logos on all pages.
- Add New page: client coverage. A page to showcase new client coverage. Could be print, links to online video, mepgs, etc. Perhaps as a blog?
- Add New page: Advertising (as a service).

Home page. Perhaps a larger image existing image can be used or something new that says Stand out from the crowd (but not in a clichéd way). perhaps 3-4 main images could be used which rotate? We want to use stunning image(s) on the site.
Retain existing body of text somewhere on page.

an alternative idea might be to look at images which relate to news. and use the phrase "journalists reaching journalists"

Add Small ‘boxes’ on home page – teasers for content inside the site:
- Our clients logo box. Perhaps use a mouse over to ‘roll’ logos from homepage? Plus link to our clients page. http://www.lanternco.example.nz/OurClients/CurrentClients.aspx
- Our services
- Quotes about us. Show an image of Harbourline magazine with quote about us
- Advertising box: Featured project (as embedded youtube clip and link case study)
- Contact us page – refresh look simple details only.

Client News (blog) page:

Image(s) to top right rather than bottom.
Google Plus like one and share as first icon. Also facebook, twitter share and RSS. (moving icons which scroll down as reader moves down?)

Hi Budget on this project to redesign Auckland PR Firm Lantern Co's website in wordpress has been increased significantly to A$2190

Target Market(s)

Marketing managers, small - large business owners
we are primarily a public relations firm, then advertising. focus should be on these services rather than web design/seo etc which are a secondary part of our offering.

Industry/Entity Type

Advertising

Requirements
Must have
• must retain existing text content(for seo reasons)
fast loading, free of slow graphics
mobile/tablet friendly
new logo
Google Plus 1 logo
Should not have
• our agency is slightly on the conservative side and yet we are looking for a modern look.
prefer light over dark colour scheme/images
Images – better to not use people in images. people from stock images tend to give the impression of an international site and we are looking closer to NZ

```html
<!DOCTYPE html>
<html lang="en">
<head>
<meta charset="utf-8">
<title>Lantern Co – Public Relations &amp; Advertising</title>
<link href="https://fonts.googleapis.com/css2?family=Questrial&family=Noto+Serif:wght@400;700&display=swap" rel="stylesheet">
<style>
  :root {
    --orange: #f26a21;
    --orange-light: #f7941d;
    --orange-dark: #ee5a1f;
    --ink: #2b2b2b;
    --grey-text: #444;
    --panel-grey: #737373;
    --page-bg: #e9e9e9;
    --white: #ffffff;
    --rule-dark: #3f3f3f;
    --box-border: #d6d6d6;
  }
  * { box-sizing: border-box; margin: 0; padding: 0; }
  html, body { width: 1200px; height: 972px; overflow: hidden; }
  body {
    position: relative;
    background: radial-gradient(ellipse at 50% 40%, #f4f4f4 0%, var(--page-bg) 70%, #dcdcdc 100%);
    font-family: "Noto Serif", Georgia, serif;
    color: var(--ink);
  }
  .abs { position: absolute; }

  /* Header */
  .brand {
    left: 134px; top: 32px;
    font-family: "Questrial", sans-serif;
    font-size: 30px; letter-spacing: 9px; color: #4a4a4a;
  }
  .social { top: 34px; left: 643px; display: flex; gap: 6px; }
  .social span {
    width: 31px; height: 31px; border-radius: 50%;
    background: linear-gradient(#fff, #e4e4e4); border: 1px solid #bdbdbd;
    display: block;
  }
  .search {
    left: 800px; top: 38px; width: 218px; height: 24px;
    background: var(--white); border: 2px solid #9a9a9a;
    font-size: 12px; color: #999; padding: 3px 6px;
  }
  .search svg { position: absolute; right: 4px; top: 3px; }
  .login {
    left: 1023px; top: 33px; width: 84px; height: 32px; border-radius: 3px;
    background: linear-gradient(var(--orange-light), var(--orange));
    color: var(--white); font-family: "Questrial", sans-serif; font-size: 14px;
    text-align: center; line-height: 32px;
  }

  /* Navigation */
  .nav-band {
    left: 0; top: 81px; width: 1200px; height: 70px;
    background: linear-gradient(var(--orange-light) 0 51%, var(--orange-dark) 51% 100%);
  }
  .nav { left: 120px; top: 92px; display: flex; height: 48px; }
  .nav a {
    display: block; text-decoration: none; color: var(--white);
    font-family: "Questrial", sans-serif; font-size: 19px; line-height: 48px; text-align: center;
    border-left: 1px solid rgba(255,255,255,.85);
  }
  .nav a:first-child { border-left: 0; color: var(--ink); }

  /* Slider */
  .slider { left: 110px; top: 163px; width: 960px; height: 280px; box-shadow: 0 6px 10px rgba(0,0,0,.2); }
  .slide-image {
    left: 0; top: 0; width: 648px; height: 280px;
    background: linear-gradient(100deg, #f2f2f2 0%, #e6e6e6 40%, #cfcfcf 70%, #e9e9e9 100%);
  }
  .slide-caption {
    left: 648px; top: 0; width: 312px; height: 280px;
    background: var(--panel-grey); color: var(--white); padding: 22px 18px;
  }
  .slide-caption h2 { font-family: "Questrial", sans-serif; font-weight: 400; font-size: 25px; line-height: 28px; }
  .slide-caption h3 { font-size: 13px; font-weight: 700; margin-bottom: 20px; }
  .slide-caption p { font-size: 12px; line-height: 20px; color: #f0f0f0; }
  .arrow {
    top: 283px; width: 40px; height: 40px; border-radius: 3px;
    background: linear-gradient(var(--orange-light), var(--orange));
    box-shadow: 0 2px 4px rgba(0,0,0,.3);
  }
  .arrow svg { position: absolute; left: 13px; top: 12px; }

  /* Intro */
  .welcome { left: 110px; top: 468px; font-family: "Questrial", sans-serif; font-size: 24px; color: #333; }
  .welcome .brand-inline { letter-spacing: 7px; font-size: 21px; }
  .tagline { left: 110px; top: 493px; font-family: "Questrial", sans-serif; font-size: 34px; color: var(--orange); }
  .intro { left: 110px; top: 550px; width: 615px; font-size: 12.6px; font-weight: 700; line-height: 20px; color: var(--ink); }
  .intro p + p { margin-top: 20px; }

  .feature { top: 745px; width: 300px; }
  .feature .thumb { position: absolute; left: 0; top: 5px; width: 58px; height: 70px; border-radius: 3px; }
  .feature .body { margin-left: 72px; font-size: 12.4px; line-height: 20px; color: var(--grey-text); }
  .feature h4 { font-size: 13px; color: var(--ink); }

  /* Sidebar */
  .side-box {
    left: 758px; width: 312px; background: var(--white);
    border: 1px solid var(--box-border); border-top: 4px solid var(--orange);
    padding: 12px 17px;
  }
  .side-box h3 { font-family: "Questrial", sans-serif; font-weight: 400; font-size: 17px; color: #333; }
  .side-box .toggles { position: absolute; right: 14px; top: 14px; }
  .project { display: flex; margin-top: 18px; }
  .project .thumb { width: 60px; height: 60px; flex: none; margin-right: 12px; }
  .project h4 { font-size: 13px; margin-bottom: 4px; }
  .project p, .news p { font-size: 12px; line-height: 20px; color: var(--grey-text); }
  .news h4 { font-size: 12.5px; margin-top: 18px; }
  .news p { color: var(--ink); line-height: 18px; }

  /* Footer */
  .footer-rule { top: 880px; height: 4px; }
  .footer-links { left: 0; top: 903px; width: 1116px; text-align: center; font-size: 13px; color: #333; }
  .footer-links span { margin: 0 5px; }
  .copyright { left: 110px; top: 937px; font-size: 12.5px; color: #333; }
</style>
</head>
<body>

<header>
  <div class="abs brand">LANTERN CO</div>
  <div class="abs social" aria-label="Social links">
    <span></span><span></span><span></span><span></span>
  </div>
  <div class="abs search">search here...
    <svg width="16" height="16" viewBox="0 0 16 16"><circle cx="9" cy="6" r="4.5" fill="none" stroke="#333" stroke-width="2"/><line x1="6" y1="9" x2="2" y2="14" stroke="#333" stroke-width="2.5"/></svg>
  </div>
  <div class="abs login">LOGIN</div>
</header>

<div class="abs nav-band"></div>
<nav class="abs nav">
  <a href="#" style="width:140px">Home</a>
  <a href="#" style="width:147px">Our Sevices</a>
  <a href="#" style="width:149px">News</a>
  <a href="#" style="width:149px">Our People</a>
  <a href="#" style="width:142px">Case Studies</a>
  <a href="#" style="width:148px">Our Clients</a>
  <a href="#" style="width:136px">Contact Us</a>
</nav>

<section class="abs slider">
  <div class="abs slide-image" role="img" aria-label="Photo of a coffee cup beside a notebook with a light bulb sketch and a hand holding a pen"></div>
  <div class="abs slide-caption">
    <h2>Lorem ipsum dolor sit</h2>
    <h3>Sed ut perspiciatis unde omnis iste</h3>
    <p>Proin tempus euismod placerat. Ut tempus purus orci, eu aliquet lorem aliquam erat volutpat. Nam leo ligula consequat sed cursus nec, eleifend sit amet neque. Ut quam diam, pellentesque sed vehicula vitae tincidunt sit amet est. Quisque gravida nibh ac nisl tincid-unt lobortis arum rerum hic tenetur.</p>
  </div>
</section>
<div class="abs arrow" style="left:87px"><svg width="12" height="16" viewBox="0 0 12 16"><path d="M9 2 3 8l6 6" fill="none" stroke="#fff" stroke-width="3"/></svg></div>
<div class="abs arrow" style="left:1052px"><svg width="12" height="16" viewBox="0 0 12 16"><path d="M3 2l6 6-6 6" fill="none" stroke="#fff" stroke-width="3"/></svg></div>

<main>
  <h1 class="abs welcome">Welcome to <span class="brand-inline">LANTERN CO</span></h1>
  <h2 class="abs tagline">Stand out from the Crowd!</h2>
  <div class="abs intro">
    <p>At vero eos et accusamus et iusto odio dignissimos ducimus qui blanditiis praesentium volup-tatum deleniti atque corrupti quos dolores et quas molestias excepturi sint occaecati cupidi-tate non provident, similique sunt in culpa qui officia deserunt mollitia animi, id est labo-rum et dolorum fuga. Et harum quidem rerum facilis est et expedita distinctio.</p>
    <p>Nam libero tempore, cum soluta nobis est eligendi optio cumque nihil impedit quo minus id quod maxime placeat facere possimus, omnis voluptas assumenda est, omnis dolor repellen-</p>
  </div>

  <div class="abs feature" style="left:115px">
    <div class="thumb" role="img" aria-label="Report document with a line chart" style="background:linear-gradient(#fafafa,#dcdcdc)"></div>
    <div class="body"><h4>Voluptatem accusantium</h4>Doloremque laudantium, totam rem aperiam, eaque ipsa quae ab illo inventore veritatis et quasi archi-tecto beatae vitae dicta sunt expli.</div>
  </div>
  <div class="abs feature" style="left:434px;width:290px">
    <div class="thumb" role="img" aria-label="Red portfolio binder" style="background:linear-gradient(90deg,#8e1b17,#c4322a)"></div>
    <div class="body"><h4>Duis aute irure dolor in</h4>Repre henderit in voluptate velit esse cillum dolore eu fugiat nulla pariatur. Excepteur sint occaecat cupidatat non proident sunt inulpa.</div>
  </div>
</main>

<aside>
  <div class="abs side-box" style="top:474px;height:226px">
    <h3>Current Projects</h3>
    <svg class="toggles" width="26" height="10" viewBox="0 0 26 10"><path d="M1 9l4-7 4 7M17 2l4 7 4-7" fill="none" stroke="#333" stroke-width="1.3"/></svg>
    <div class="project">
      <div class="thumb" role="img" aria-label="Classical building columns under blue sky" style="background:linear-gradient(#1f5aa8,#c9b48a)"></div>
      <div><h4>Deleniti atque</h4><p>Corrupti quos dolores et quas mo-lestias excepturi sint occaecati.</p></div>
    </div>
    <div class="project">
      <div class="thumb" role="img" aria-label="Bronze statue against blue sky" style="background:linear-gradient(#4f7fb8,#6b6e5a)"></div>
      <div><h4>Quibusdam et aut</h4><p>Similique sunt in culpa qui officia deserunt mollitia animi id est.</p></div>
    </div>
  </div>

  <div class="abs side-box news" style="top:714px;height:146px">
    <h3>Latest News</h3>
    <svg class="toggles" width="26" height="10" viewBox="0 0 26 10"><path d="M1 9l4-7 4 7M17 2l4 7 4-7" fill="none" stroke="#333" stroke-width="1.3"/></svg>
    <h4>March 5, 2013</h4>
    <p>Corrupti quos dolores et quas molestias excep-turi sint occaecati praesent nisl erat, pharetra mollis commodo a, consectetur ut mi.</p>
  </div>
</aside>

<footer>
  <div class="abs footer-rule" style="left:110px;width:648px;background:var(--rule-dark)"></div>
  <div class="abs footer-rule" style="left:758px;width:312px;background:var(--orange)"></div>
  <div class="abs footer-links">Home<span>|</span>News<span>|</span>Our Services<span>|</span>Our People<span>|</span>Case Studies<span>|</span>Our Clients<span>|</span>Contact us<span>|</span>Terms Of Use<span>|</span> Privacy Statement<span>|</span>Login</div>
  <div class="abs copyright">Copyright © 2012 <b>Lantern Co Limited.</b> &nbsp;All rights reserved.</div>
</footer>

</body>
</html>
```